Fun and Flirty Urban Fiction Book Needs a Book Cover Design

We need an e-book cover designed for a title called Dazzle Dazzle SEQUIN STORM.

We require:

1. 3 sexy and provocative African-American female models who look similar to the girl in the green shorts on the cover provided entitled Cool Cat Charmer.

2. A set of beautiful and shapely twins (they are the Dazzle Dazzle in the title) and then an equally shapely and beautiful model in scanty attire (she is the SEQUIN STORM) in the title.

3. We need vibrant and sexy colors and dynamic fonts, whose FONT examples are provided in the upload.

Very Important!

1. The fonts for the words Dazzle Dazzle should match the font for the word Dazzle on the green cover attached. (Cool Cat Charmer).

2. The fonts for the words Sequin Storm must match the fonts for the words Sequin Storm on the orange cover attached. (Sequin Storm).

3. The cover colors must be vibrant and upbeat. This is a FUN and "flirty" novel.

4. The author's names should appear as by Velour and Tasha Bay.

Please look at the series of bookcovers that are attached!!!

5. The cover must fit in with the theme of the book covers provided. That means, there must be some white on the cover, on the right hand side, and then faded into the rest of the background.

6. The title should take up a large portion of the cover, as it does in the covers provided.

7. The sub-title should say: The Escapades of Coco Delane featuring Peachee Kane. See fonts on the covers provided.

8. The author name VELOUR must be in the same font as on the covers provided, preferably in 3D with the words Vantage Bestselling Author above it.

9. The author name Tasha Bay can be in a different font.

DESIGNERS SHOULD LOOK AT EXAMPLE COVERS AND FONTS PROVIDED AND MAKE THIS COVER FIT INTO THE THEME OF THE PREVIOUS BOOKS.

Target Market(s)

Fiction readers ages 18-50.

Font styles to use
Script
Other font styles liked:
• Fonts similar to those provided in the upload

Requirements
Must have
• Please look at the series of bookcovers that are attached!!!
• 1. The cover must fit in with the theme of the book covers provided. That means, there must be some white on the cover, on the right hand side, and then faded into the rest of the background.
• 2. The title should take up a large portion of the cover, as it does in the covers provided.
• 3. The sub-title should say: The Escapades of Coco Delane featuring Peachee Kane
• 4. The author name VELOUR must be in the same font as on the covers provided, preferably in 3D.
• 5. The author name Tasha Bay can be in a different font.
• Three beautiful biracial or African American female models who look similar to the girl described on the green book titled COOL CAT CHARMER. Fonts similar to those provided in the project description. A fun, sexy, urban flair.
Nice to have
• Shapely, devious and beautiful models
Should not have
• Thin models who are not either bi-racial or African American.

```html
<!DOCTYPE html>
<html lang="en">
<head>
<meta charset="utf-8">
<title>Dazzle Dazzle Sequin Storm — Book Cover</title>
<link rel="stylesheet" href="https://fonts.googleapis.com/css2?family=Anton&family=Pinyon+Script&family=Playfair+Display:wght@900&family=Roboto+Condensed:wght@400;700&family=Roboto:ital@0;1&display=swap">
<style>
  :root {
    --bg: #e6e6e6;
    --paper: #ffffff;
    --flame-red: #e2321f;
    --deep-red: #9e1410;
    --ink: #150606;
    --ember: #f28a1c;
    --dusk: #6a2a70;
  }
  * { margin: 0; padding: 0; box-sizing: border-box; }
  html, body { width: 1200px; height: 1200px; overflow: hidden; background: var(--bg); }
  .cover {
    position: absolute; left: 152px; top: 20px;
    width: 895px; height: 1160px;
    background: var(--paper); overflow: hidden;
  }
  .cover-art { position: absolute; inset: 0; width: 100%; height: 100%; }
  .tagline {
    position: absolute; left: 595px; top: 80px; width: 270px;
    font-family: "Roboto", sans-serif; font-size: 17px; line-height: 21px;
    text-align: center; color: var(--ink);
  }
  .tagline em { font-style: italic; }
  .author-kicker {
    position: absolute; right: 60px; top: 250px;
    font-family: "Roboto Condensed", sans-serif; font-weight: 700;
    font-size: 15px; letter-spacing: 2px; text-transform: uppercase;
    color: var(--ink);
  }
  .author-lead {
    position: absolute; right: 58px; top: 270px;
    font-family: "Anton", sans-serif; font-size: 112px; line-height: 1;
    font-weight: 400;
    color: var(--flame-red); -webkit-text-stroke: 2px var(--ink);
    text-shadow: 3px 3px 0 var(--deep-red), 5px 5px 3px rgba(0,0,0,.3);
  }
  .author-co {
    position: absolute; right: 60px; top: 382px;
    font-family: "Roboto Condensed", sans-serif; font-weight: 700;
    font-size: 32px; line-height: 1; color: var(--deep-red);
  }
  .author-co .amp { color: var(--ink); font-weight: 400; }
  .title-script {
    position: absolute; font-family: "Pinyon Script", cursive;
    font-size: 132px; line-height: 1; color: var(--flame-red);
    -webkit-text-stroke: 0.8px var(--ink);
    white-space: nowrap;
  }
  .title-script.first { left: 320px; top: 392px; }
  .title-script.second { left: 425px; top: 530px; }
  .title-block {
    position: absolute; right: 52px; top: 705px; text-align: right;
    font-family: "Playfair Display", serif; font-weight: 900;
    font-size: 100px; line-height: 106px; color: var(--ink);
    -webkit-text-stroke: 2px var(--flame-red);
    text-shadow: 3px 3px 4px rgba(0,0,0,.35);
  }
  .subtitle {
    position: absolute; left: 560px; top: 962px; width: 270px;
    text-align: center; color: var(--ink);
  }
  .subtitle .script { font-family: "Pinyon Script", cursive; font-size: 36px; line-height: 38px; }
  .subtitle .name { font-family: "Roboto Condensed", sans-serif; font-weight: 700; font-size: 24px; line-height: 30px; }
  .subtitle .feat { font-family: "Roboto Condensed", sans-serif; font-size: 24px; line-height: 30px; }
  .subtitle .feat b { font-weight: 700; }
</style>
</head>
<body>
<main class="cover">
  <svg class="cover-art" viewBox="0 0 895 1160" aria-hidden="true">
    <defs>
      <linearGradient id="fadeAcross" x1="0" y1="0" x2="1" y2="0">
        <stop offset="0" stop-color="#b81a12"/>
        <stop offset="0.5" stop-color="#d42a1c"/>
        <stop offset="0.66" stop-color="#c93a2e" stop-opacity="0.6"/>
        <stop offset="0.8" stop-color="#ffffff" stop-opacity="0"/>
      </linearGradient>
      <radialGradient id="duskGlow" cx="0.62" cy="0.2" r="0.28">
        <stop offset="0" stop-color="#8a3a8a" stop-opacity="0.55"/>
        <stop offset="1" stop-color="#8a3a8a" stop-opacity="0"/>
      </radialGradient>
      <radialGradient id="emberGlow" cx="0.45" cy="1" r="0.45">
        <stop offset="0" stop-color="#f28a1c" stop-opacity="0.95"/>
        <stop offset="1" stop-color="#f28a1c" stop-opacity="0"/>
      </radialGradient>
      <linearGradient id="shadowTop" x1="0" y1="0" x2="0.4" y2="0.4">
        <stop offset="0" stop-color="#150606" stop-opacity="0.75"/>
        <stop offset="1" stop-color="#150606" stop-opacity="0"/>
      </linearGradient>
      <linearGradient id="figureTone" x1="0" y1="0" x2="0" y2="1">
        <stop offset="0" stop-color="#3a0808"/>
        <stop offset="0.35" stop-color="#8e1612"/>
        <stop offset="0.7" stop-color="#6b0f0c"/>
        <stop offset="1" stop-color="#c0281a"/>
      </linearGradient>
    </defs>
    <rect width="895" height="1160" fill="#ffffff"/>
    <rect width="895" height="1160" fill="url(#fadeAcross)"/>
    <rect width="895" height="1160" fill="url(#duskGlow)"/>
    <rect width="895" height="1160" fill="url(#shadowTop)"/>
    <g role="img" aria-label="Photo of a curvy model in a black strapless bikini, tinted red, hand resting on her hip">
      <path d="M0 240 C120 200 300 210 390 230 C410 330 420 420 460 520 C520 640 540 760 520 900 C500 1000 430 1080 380 1160 L0 1160 Z"
            fill="url(#figureTone)" opacity="0.85"/>
    </g>
    <rect width="895" height="1160" fill="url(#emberGlow)"/>
  </svg>

  <p class="tagline">What happens when<br>the Dazzle meets the Storm?<br><em>There can only be one<br>Queen of Harlem.</em><br>Will it be<br>#TeamCoco or #TeamPeachee?</p>

  <p class="author-kicker">Vantage Bestselling Author</p>
  <h2 class="author-lead">VELOUR</h2>
  <p class="author-co"><span class="amp">&amp;</span> Tasha Bay</p>

  <h1>
    <span class="title-script first">Dazzle</span>
    <span class="title-script second">Dazzle</span>
    <span class="title-block">SEQUIN<br>STORM</span>
  </h1>

  <div class="subtitle">
    <p class="script">The<br>Escapades of</p>
    <p class="name">Coco Delane</p>
    <p class="feat">featuring <b>Peachee Kane</b></p>
  </div>
</main>
</body>
</html>
```